Birthday Party Invitation for Jasper's 18th Birthday Party

Our eldest son Jasper is turning 18 and we are having a party at home to celebrate the occasion. This project is about creating an invitation that will go to our friends and family. We like things to be nicely designed so posting it to print flock seemed to be the way to go.
The invitation needs to be able to be printed onto an A4 piece of paper. We have access to a color copier so it can be nice and bright.

We want an invitation that conveys a sense of occasion and looks as though we have put time and effort into having a great night to celebrate his 18th.
I have included some photo's of Jasper. They can go onto the invitation as is or they can be given some treatment to form a theme when on the invitiation. I'll leave the treatment of the photo's to the individual designer.

Target Market(s)

Friends and Family

Font styles to use
Sans Serif

Colors

Designer to choose colors to be used in the design.

Requirements
Must have
• The invitation must have the time, date and location of the party.
• Details:
• Saturday 29th of July 2017 7.00pm
• 41 Marbrook Lane, Fenhollow
• Food and Drinks provided It must be bright and colourful and convey a sense of excitement.
Nice to have
• Inclusion of the photo's that I have uploaded.
Should not have
• any boring bits

```html
<!DOCTYPE html>
<html lang="en">
<head>
<meta charset="utf-8">
<title>Jasper's Eighteenth Birthday</title>
<link rel="stylesheet" href="https://fonts.googleapis.com/css2?family=Bodoni+Moda:wght@500&family=Great+Vibes&family=Josefin+Sans:wght@400&display=swap">
<style>
  :root {
    --bg: #262626;
    --gold: #d9a53a;
    --gold-light: #f2cd78;
    --gold-deep: #a87a26;
    --white: #ffffff;
  }
  * { margin: 0; padding: 0; box-sizing: border-box; }
  html, body { width: 846px; height: 1200px; overflow: hidden; background: var(--bg); }
  .invitation {
    position: relative;
    width: 846px;
    height: 1200px;
    background: var(--bg);
    overflow: hidden;
  }
  .confetti-top {
    position: absolute;
    left: 0; top: 0;
    width: 846px; height: 130px;
    background: linear-gradient(180deg, var(--gold) 0%, rgba(217,165,58,0.55) 45%, rgba(217,165,58,0) 100%);
  }
  .age-numeral {
    position: absolute;
    left: 0; top: 0;
    width: 846px; height: 720px;
  }
  .age-numeral text {
    font-family: "Bodoni Moda", serif;
    font-weight: 500;
  }
  .title {
    position: absolute;
    left: 0; top: 728px;
    width: 846px;
    text-align: center;
    font-family: "Great Vibes", cursive;
    font-size: 70px;
    line-height: 1;
    color: var(--white);
  }
  .details {
    position: absolute;
    left: 0; top: 855px;
    width: 846px;
    text-align: center;
    list-style: none;
    font-family: "Josefin Sans", sans-serif;
    font-size: 19px;
    letter-spacing: 2px;
    line-height: 31px;
    text-transform: uppercase;
    color: var(--white);
  }
  .photo-strip {
    position: absolute;
    left: 29px; top: 978px;
    width: 788px; height: 160px;
    display: flex;
    gap: 10px;
  }
  .photo { flex: 1; height: 160px; }
  .photo--sailing { background: linear-gradient(180deg, #bcd6ea, #2f6e9c); }
  .photo--harbour { background: linear-gradient(180deg, #cfe0ee, #5b6a78); }
  .photo--blazer { background: linear-gradient(180deg, #8fb3c9, #3a2a2e); }
  .photo--family { background: linear-gradient(180deg, #5d6b3c, #2d3340); }
  .photo--waterpolo { background: linear-gradient(180deg, #5aa6d6, #1f78b8); }
  .photo--siblings { background: linear-gradient(180deg, #6f8f4a, #b9a99a); }
  .confetti-bottom {
    position: absolute;
    left: 0; top: 1080px;
    width: 846px; height: 120px;
    background: linear-gradient(0deg, var(--gold) 0%, rgba(217,165,58,0.7) 55%, rgba(217,165,58,0) 100%);
  }
</style>
</head>
<body>
<main class="invitation">
  <div class="confetti-top" role="img" aria-label="Gold confetti dots scattered along the top edge"></div>

  <svg class="age-numeral" viewBox="0 0 846 720" aria-label="18">
    <defs>
      <linearGradient id="gold-fill" x1="0" y1="0" x2="1" y2="1">
        <stop offset="0" stop-color="#f2cd78"/>
        <stop offset="0.5" stop-color="#d9a53a"/>
        <stop offset="1" stop-color="#a87a26"/>
      </linearGradient>
    </defs>
    <text x="99" y="684" font-size="770" textLength="650" lengthAdjust="spacingAndGlyphs" fill="url(#gold-fill)">18</text>
  </svg>

  <h1 class="title">Jasper's Eighteenth Birthday</h1>

  <ul class="details">
    <li>Saturday 29th of July 2017 7.00pm</li>
    <li>41 Marbrook Lane, Fenhollow</li>
    <li>Food and drinks provided</li>
  </ul>

  <div class="photo-strip">
    <div class="photo photo--sailing" role="img" aria-label="Photo of Jasper sailing a small dinghy"></div>
    <div class="photo photo--harbour" role="img" aria-label="Photo of Jasper in front of a harbour bridge"></div>
    <div class="photo photo--blazer" role="img" aria-label="Photo of Jasper in a striped school blazer"></div>
    <div class="photo photo--family" role="img" aria-label="Photo of Jasper with his parents"></div>
    <div class="photo photo--waterpolo" role="img" aria-label="Photo of Jasper playing water polo"></div>
    <div class="photo photo--siblings" role="img" aria-label="Photo of Jasper with his sister in a garden"></div>
  </div>

  <div class="confetti-bottom" role="img" aria-label="Gold confetti dots scattered along the bottom edge"></div>
</main>
</body>
</html>
```